Seven nights at the harbour

Creation of the cover for the book: "Sept nuits sur le quai du port" with the joined photo of a 70 years old lady.
Title: "Seven nights along the old harbour"
Author: "Mireille Vaston"
Publisher: "Editions Morvane" (should be at the bottom of the page)
Format: 14 x 20.5 cm
The story: A senior lady (70 years old), divorced, with a beautiful face, still wants to seduce, even young men.
We found the perfect photo for the woman. We would like to ask you to make a modern cover from it.
Besoin de quelques jours pour choisir un design
Target Market(s)
Novels reader (adults)
Industry/Entity Type
book

```html
<!DOCTYPE html>
<html lang="en">
<head>
<meta charset="utf-8">
<title>Seven nights along the old harbour — cover wrap</title>
<link rel="stylesheet" href="https://fonts.googleapis.com/css2?family=Montserrat:wght@800&family=Sacramento&family=Source+Sans+3:wght@400;600&display=swap">
<style>
  :root {
    --ink: #000000;
    --pink: #ff0a6c;
    --white: #ffffff;
    --silver: #b9b9b9;
    --skin: #7a3a28;
  }
  * { margin: 0; padding: 0; box-sizing: border-box; }
  html, body { width: 1200px; height: 796px; overflow: hidden; background: var(--ink); }
  .wrap { position: relative; width: 1200px; height: 796px; background: var(--ink); overflow: hidden; }

  .display { font-family: "Montserrat", sans-serif; font-weight: 800; color: var(--pink); line-height: 1; white-space: nowrap; letter-spacing: 0; }
  .script { font-family: "Sacramento", cursive; color: var(--white); line-height: 1; white-space: nowrap; }

  /* Back cover */
  .back { position: absolute; left: 0; top: 0; width: 583px; height: 796px; }
  .back-title { position: absolute; left: 0; width: 532px; top: 112px; text-align: center; }
  .back-title .line-top { font-size: 46px; display: block; }
  .back-title .line-mid { font-size: 40px; display: block; margin-top: -14px; position: relative; z-index: 2; }
  .back-title .line-bottom { font-size: 62px; display: block; margin-top: -20px; }
  .blurb { position: absolute; left: 61px; width: 410px; top: 262px; font-family: "Source Sans 3", sans-serif; font-size: 14.2px; line-height: 25.8px; color: var(--white); }
  .blurb p { text-align: justify; text-align-last: center; margin-bottom: 25.8px; }

  /* Spine */
  .spine { position: absolute; left: 583px; top: 40px; width: 38px; height: 730px; writing-mode: vertical-rl; display: flex; align-items: center; gap: 10px; }
  .spine .display { font-size: 29px; }
  .spine .spine-mid { font-size: 28px; }
  .spine .spine-author { font-size: 34px; margin-top: 22px; }

  /* Front cover */
  .front { position: absolute; left: 670px; top: 0; width: 530px; height: 796px; }
  .front-photo {
    position: absolute; inset: 0;
    background:
      radial-gradient(ellipse 30% 22% at 68% 47%, rgba(150, 70, 50, 0.55), transparent 70%),
      radial-gradient(ellipse 55% 45% at 55% 40%, rgba(185, 185, 185, 0.55), transparent 75%),
      radial-gradient(ellipse 60% 40% at 40% 70%, rgba(140, 140, 140, 0.35), transparent 75%),
      linear-gradient(180deg, #0a0a0a 0%, #262626 45%, #141414 80%, #050505 100%);
  }
  .front-title { position: absolute; left: 0; right: 0; top: 50px; text-align: center; }
  .front-title .line-top { font-size: 60px; display: block; }
  .front-title .line-mid { font-size: 58px; display: block; margin-top: -14px; position: relative; z-index: 2; }
  .front-title .line-bottom { font-size: 82px; display: block; margin-top: -24px; }
  .front-author { position: absolute; left: 0; right: 0; top: 612px; text-align: center; font-size: 78px; }
  .publisher { position: absolute; left: 0; right: 0; top: 734px; text-align: center; font-family: "Source Sans 3", sans-serif; font-weight: 600; font-size: 12.5px; letter-spacing: 1.2px; color: var(--white); }
</style>
</head>
<body>
<main class="wrap">
  <section class="back">
    <h2 class="back-title">
      <span class="display line-top">SEVEN NIGHTS</span>
      <span class="script line-mid">along the old</span>
      <span class="display line-bottom">HARBOUR</span>
    </h2>
    <div class="blurb">
      <p>A senior lady (70 years old), divorced, with a beautiful face, still wants to seduce, even young men.We found the perfect photo for the woman. We would like to ask you to make a modern cover from it.A senior lady (70 years old), divorced, with a beautiful face, still wants to seduce, even young men.</p>
      <p>We found the perfect photo for the woman. We would like to ask you to make a modern cover from it.A senior lady (70 years old), divorced, with a beautiful face, still wants to seduce, even young men. We found the perfect photo for the woman. We would like to ask you to make a modern cover from it.A senior lady (70 years old), divorced, with a beautiful face, still wants to seduce, even young men.</p>
      <p>We found the perfect photo for the woman. We would like to ask you to make a modern cover from it.</p>
    </div>
  </section>

  <section class="spine">
    <span class="display">SEVEN NIGHTS</span>
    <span class="script spine-mid">along the old</span>
    <span class="display">HARBOUR</span>
    <span class="script spine-author">Mireille Vaston</span>
  </section>

  <section class="front">
    <div class="front-photo" role="img" aria-label="Close-up photograph of a senior woman's face veiled by long silver-grey hair, lips visible, on a black background"></div>
    <h1 class="front-title">
      <span class="display line-top">SEVEN NIGHTS</span>
      <span class="script line-mid">along the old</span>
      <span class="display line-bottom">HARBOUR</span>
    </h1>
    <p class="script front-author">Mireille Vaston</p>
    <p class="publisher">PUBLISHER : EDITIONS MORVANE</p>
  </section>
</main>
</body>
</html>
```